I would like a business card to match my truck wrap and logo. I would like the font to match my existing business card please.

Industry/Entity Type

Painter

Contact Information for Business Card

Rodrigo Venaza 801-437-2916 Venazacoatings.utah@brushmail.net
SERVICES - Custom Paint & Stain, Interior & Exterior, Epoxy Coatings / Garage Floors, Cabinet Refinishing, Log Staining and Refinishing.

Requirements
Nice to have
• I would like to have the white and grey line like the bottom of my vehicle wrap, Light Grey to match my truck also.

```html
<!DOCTYPE html>
<html lang="en">
<head>
<meta charset="utf-8">
<title>Venaza Coatings – Business Card</title>
<link rel="stylesheet" href="https://fonts.googleapis.com/css2?family=Michroma&family=Exo+2:wght@300;400&display=swap">
<style>
  :root {
    --stage: #000000;
    --card: #ffffff;
    --band-grey: #c3cad2;
    --brand-blue: #1aa3e8;
    --deep-blue: #1b6fb5;
  }
  * { margin: 0; padding: 0; box-sizing: border-box; }
  html, body { width: 1200px; height: 1000px; overflow: hidden; background: var(--stage); }
  .stage { position: relative; width: 1200px; height: 1000px; }
  .card {
    position: absolute; left: 509px; width: 559px; height: 350px;
    background: var(--card); overflow: hidden;
  }
  .card--front { top: 126px; }
  .card--back { top: 524px; }
  .card svg.bands { position: absolute; left: 0; top: 0; width: 559px; height: 350px; }
  .band { fill: var(--band-grey); }

  .wordmark {
    position: absolute; left: 62px; top: 92px;
    display: flex; align-items: center; gap: 22px;
    font-family: "Michroma", sans-serif; font-weight: 400; color: var(--brand-blue);
  }
  .wordmark__square { width: 92px; height: 92px; background: var(--deep-blue); }
  .wordmark__name { display: flex; flex-direction: column; line-height: 1; }
  .wordmark__primary { font-size: 40px; letter-spacing: 1px; }
  .wordmark__secondary { font-size: 15px; letter-spacing: 8.5px; margin-top: 10px; }

  .contact { position: absolute; left: 41px; top: 45px; color: var(--brand-blue); }
  .contact__name { font-family: "Michroma", sans-serif; font-size: 16px; letter-spacing: 0.5px; }
  .contact__email { font-family: "Exo 2", sans-serif; font-weight: 400; font-size: 14.5px; margin-top: 3px; }
  .contact__phone { font-family: "Michroma", sans-serif; font-size: 15px; letter-spacing: 1.5px; margin-top: 17px; }
  .services { position: absolute; left: 42px; top: 138px; color: var(--brand-blue); width: 230px; }
  .services__title { font-family: "Michroma", sans-serif; font-size: 13px; letter-spacing: 0.5px; }
  .services__list { font-family: "Exo 2", sans-serif; font-weight: 300; font-size: 14.5px; line-height: 18px; }
  .back-mark { position: absolute; left: 418px; top: 215px; width: 72px; height: 72px; background: var(--deep-blue); }
</style>
</head>
<body>
<div class="stage">

  <section class="card card--front">
    <div class="wordmark">
      <div class="wordmark__square"></div>
      <div class="wordmark__name">
        <span class="wordmark__primary">VENAZA</span>
        <span class="wordmark__secondary">COATINGS</span>
      </div>
    </div>
    <svg class="bands" viewBox="0 0 559 350" aria-hidden="true">
      <rect class="band" x="0" y="279" width="559" height="10"/>
      <rect class="band" x="0" y="301" width="559" height="49"/>
    </svg>
  </section>

  <section class="card card--back">
    <svg class="bands" viewBox="0 0 559 350" aria-hidden="true">
      <polygon class="band" points="0,279 286,279 436,131 559,131 559,141 440,141 290,289 0,289"/>
      <polygon class="band" points="0,301 296,301 451,154 559,154 559,350 0,350"/>
    </svg>
    <div class="contact">
      <p class="contact__name">RODRIGO VENAZA</p>
      <p class="contact__email">Venazacoatings.utah@brushmail.net</p>
      <p class="contact__phone">801.437.2916</p>
    </div>
    <div class="services">
      <p class="services__title">SERVICES</p>
      <p class="services__list">Custom Paint &amp; Stain,<br>Interior &amp; Exterior, Epoxy<br>Coatings/Garage Floors,<br>Cabinet Refinishing,<br>Log Staining and<br>Refinishing.</p>
    </div>
    <div class="back-mark"></div>
  </section>

</div>
</body>
</html>
```